Business Card Design Project

We are rebranding an existing automotive collision repair business. The business is called dentworks garage. I have attached logo but I'm not tied to that. I want to leave this wide open.

I want this card to say we are professional, competent, cutting edge. We are focused on customers and use a lot of the latest technology to make the customer experience different. We sign customers in on iPads. Paperwork I signed electronically and updates are sent via text, email, logging on a website or as they wish. I want this innovation and image to come through in our cards

Target Market(s)

60%. Women 40% men. Age 35-60

Industry/Entity Type

Automotive

Requirements
Must have
• The card must have name, title, phone,email, cell, web page

```html
<!DOCTYPE html>
<html lang="en">
<head>
<meta charset="UTF-8">
<title>dentworks garage business card</title>
<link rel="stylesheet" href="https://fonts.googleapis.com/css2?family=PT+Sans+Narrow:wght@400;700&display=swap">
<style>
  :root {
    --backdrop: #e1e1e1;
    --card-light: #ffffff;
    --card-dark: #1c1c1c;
    --brand-green: #6aa92a;
    --ink: #1f1f1f;
  }
  * { margin: 0; padding: 0; box-sizing: border-box; }
  html, body { width: 1200px; height: 849px; overflow: hidden; }
  body {
    background: var(--backdrop);
    position: relative;
    font-family: "PT Sans Narrow", "Arial Narrow", sans-serif;
    color: var(--ink);
  }
  .card {
    position: absolute;
    top: 290px;
    width: 467px;
    height: 268px;
    border-radius: 14px;
    overflow: hidden;
  }
  .card--front { left: 98px; background: var(--card-light); }
  .card--back { left: 634px; background: var(--card-dark); }

  .brand {
    position: absolute;
    display: flex;
    justify-content: center;
    align-items: center;
  }
  .brand__name {
    font-family: "PT Sans Narrow", "Arial Narrow", sans-serif;
    font-weight: 700;
    color: var(--brand-green);
    line-height: 1;
    white-space: nowrap;
  }
  .card--front .brand { left: 166px; top: 17px; width: 284px; height: 72px; }
  .card--front .brand__name { font-size: 32px; }

  .card--back .brand { left: 16px; top: 68px; width: 436px; height: 110px; }
  .card--back .brand__name { font-size: 52px; }

  .person { position: absolute; left: 22px; top: 148px; }
  .person__name { font-size: 20px; color: var(--brand-green); line-height: 1; letter-spacing: -0.3px; }
  .person__title { font-size: 11px; color: var(--ink); margin-top: 2px; }

  .contact { position: absolute; left: 206px; top: 146px; list-style: none; }
  .contact__item {
    display: flex; align-items: center;
    height: 16.4px;
    font-size: 11px;
    color: var(--ink);
  }
  .contact__icon { width: 12px; height: 10px; margin-right: 13px; fill: var(--ink); }

  .card__band {
    position: absolute; left: 0; bottom: 0;
    width: 100%; height: 24px;
    background: var(--brand-green);
  }
</style>
</head>
<body>
  <section class="card card--front">
    <div class="brand">
      <span class="brand__name">dentworks garage</span>
    </div>

    <div class="person">
      <p class="person__name">Your Name</p>
      <p class="person__title">Tittle</p>
    </div>

    <ul class="contact">
      <li class="contact__item">
        <svg class="contact__icon" viewBox="0 0 12 10"><rect x="0" y="1" width="12" height="8"/><polyline points="0.5,1.5 6,6 11.5,1.5" fill="none" stroke="#fff" stroke-width="1"/></svg>
        1111 Address, xxxxxxxx xxxxxxxx -xx
      </li>
      <li class="contact__item">
        <svg class="contact__icon" viewBox="0 0 12 10"><path d="M2 1 L4 1 L5 3 L4 4 Q5 6 7 7 L8 6 L10 7 L10 9 Q5 9 2 5 Q1 3 2 1Z"/></svg>
        000 000 000
      </li>
      <li class="contact__item">
        <svg class="contact__icon" viewBox="0 0 12 10"><rect x="0" y="1" width="12" height="8" rx="1"/><circle cx="6" cy="5" r="2.3" fill="#fff"/><circle cx="6" cy="5" r="1.2"/></svg>
        e-mail : xxxx_xxx@mailbox.net
      </li>
      <li class="contact__item">
        <svg class="contact__icon" viewBox="0 0 12 10"><rect x="3" y="0" width="6" height="10" rx="1"/><rect x="4" y="1.5" width="4" height="5" fill="#fff"/></svg>
        000 000 000
      </li>
      <li class="contact__item">
        <svg class="contact__icon" viewBox="0 0 12 10"><circle cx="6" cy="5" r="4.5"/><path d="M1.5 5 H10.5 M6 0.5 V9.5" stroke="#fff" stroke-width="0.8"/></svg>
        Website : xxxxxxxx xxxx xxx xxxx xxx
      </li>
    </ul>

    <div class="card__band"></div>
  </section>

  <section class="card card--back">
    <div class="brand">
      <span class="brand__name">dentworks garage</span>
    </div>
  </section>
</body>
</html>
```